Postcard for Home Inventory business that is specific for our apartment customers.

We need a postcard that is a smaller version of one of our flyers. This postcard will be distributed to apartment complexes specifically. We will offer 10% off and 25 extra photos with presentation of this card. The front of the card should have our logo, an explanation to the customer why they need our service, and the discounts offered with the card. The back should be the apartment package pricing and the additional services. Postcard should have logo colors involved.

Target Market(s)

Apartment complexes / Renters

Industry/Entity Type

Business

Font styles to use
Serif

Requirements
Must have
• Postcard should be front and back. The front should have my logo and the 10% off discount and the 25 extra photos displayed on the front. It should also display my name (Dana Corvell as the President / Owner) the website (www.brantlofts.com), email (dana@brantlofts.com) and phone# (602-555-0143).
Nice to have
• Something similar to the flyer that I attached. Background images.

```html
<!DOCTYPE html>
<html lang="en">
<head>
<meta charset="utf-8">
<title>BRANT Home Inventory – Apartment Postcard</title>
<link href="https://fonts.googleapis.com/css2?family=Roboto+Slab:wght@400;700;900&family=PT+Serif:ital,wght@0,400;0,700;1,400&display=swap" rel="stylesheet">
<style>
:root{
  --bg:#e9e6e1;
  --ink:#1f2021;
  --ink-2:#2c2e30;
  --green:#7dc242;
  --green-dark:#5a9a28;
  --white:#ffffff;
  --red:#d8262d;
  --grey:#c9cbcd;
}
*{margin:0;padding:0;box-sizing:border-box}
html,body{width:829px;height:1200px;overflow:hidden;background:var(--bg)}
body{position:relative;font-family:"PT Serif",serif;color:var(--white)}
.card{position:absolute;left:34px;width:761px;height:560px;background:linear-gradient(160deg,var(--ink-2),var(--ink));overflow:hidden;box-shadow:0 4px 14px rgba(0,0,0,.25)}
.card--front{top:22px}
.card--back{top:612px}
.abs{position:absolute}
.heading{font-family:"Roboto Slab",serif;font-weight:900}

/* front */
.hero-photo{left:250px;top:0;width:511px;height:175px;background:linear-gradient(180deg,#6f8fb0 0%,#a7885f 60%,#2c2e30 100%);opacity:.85}
.logo{left:22px;top:22px;display:flex;align-items:center;gap:10px}
.logo__mark{width:40px;height:40px;background:var(--green)}
.logo__name{font-family:"Roboto Slab",serif;font-weight:900;font-size:44px;color:var(--white);letter-spacing:1px}
.offer{left:590px;top:28px;width:150px;height:178px}
.offer__top{background:var(--white);color:var(--red);text-align:center;padding:10px 0 6px;font-family:"Roboto Slab",serif;font-weight:900;font-size:40px;line-height:1}
.offer__bottom{background:var(--green);text-align:center;padding:10px 6px;font-family:"Roboto Slab",serif;font-weight:700;line-height:1.1}
.offer__bottom .big{font-size:28px;display:block}
.offer__bottom .small{font-size:15px;display:block}
.why{left:22px;top:182px;font-size:34px;color:var(--green)}
.why-text{left:22px;top:232px;width:450px;font-size:15.5px;line-height:1.45}
.boxes{left:480px;top:250px;width:265px;height:175px;background:linear-gradient(160deg,#d6a86a,#9b6a35);border-radius:4px}
.contact-band{left:0;top:470px;width:761px;height:90px;background:linear-gradient(90deg,var(--green-dark),var(--green))}
.call{left:22px;top:498px;font-family:"Roboto Slab",serif;font-size:30px;font-weight:700}
.call small{font-size:22px;font-weight:400;margin-right:6px}
.contact-list{left:470px;top:477px;font-size:15px;line-height:1.55}
.contact-list div{display:flex;align-items:center;gap:8px}
.contact-list .owner{font-weight:700}

/* back */
.back-photo{left:0;top:0;width:761px;height:200px;background:linear-gradient(180deg,#3b3e41,#1f2021);opacity:.9}
.bar{background:var(--green);color:var(--white);font-family:"Roboto Slab",serif;font-weight:700;font-size:17px;padding:6px 14px}
.package-bar{left:0;top:18px;width:330px}
.bullets{left:22px;top:58px;width:480px;font-size:15.5px;line-height:1.4;list-style:none}
.bullets li::before{content:"• ";color:var(--green)}
.callbox{left:520px;top:18px;width:220px;height:130px;border:2px solid var(--green);text-align:center;padding-top:12px;background:rgba(0,0,0,.35)}
.callbox .heading{font-size:38px;line-height:1}
.callbox .phone{color:var(--green);font-family:"Roboto Slab",serif;font-weight:700;font-size:20px;margin-top:6px}
.callbox .mail{font-size:13px;margin-top:4px}
.note{left:22px;top:205px;width:715px;font-size:12.5px;font-style:italic;line-height:1.4;color:var(--grey)}
.services-bar{left:0;top:282px;width:260px}
.services{left:22px;top:322px;width:720px;font-size:14px;line-height:1.5;list-style:none}
.services li::before{content:"• ";color:var(--green)}
.services b{color:var(--green)}
</style>
</head>
<body>

<section class="card card--front">
  <div class="abs hero-photo" role="img" aria-label="Photo of an apartment complex with pool at dusk"></div>
  <div class="abs logo"><span class="logo__mark"></span><span class="logo__name">BRANT</span></div>
  <div class="abs offer">
    <div class="offer__top">10%<br>OFF</div>
    <div class="offer__bottom"><span class="small">AND</span><span class="big">25</span><span class="small">EXTRA PHOTOS</span></div>
  </div>
  <h1 class="abs heading why">WHY DO I NEED BRANT?</h1>
  <p class="abs why-text">As a renter, you want to be proactive in keeping track of the contents in your home so you are prepared in case of a disaster or life-changing event. Having renters insurance is not enough as insurance companies will ask for proof of ownership in case of a fire, theft or other loss! Let the experienced professionals at BRANT perform a thorough inventory of your home so you can further protect what means most, your family and your assets.</p>
  <div class="abs boxes" role="img" aria-label="Stack of cardboard moving boxes"></div>
  <div class="abs contact-band"></div>
  <div class="abs call"><small>call us</small>602-555-0143</div>
  <div class="abs contact-list">
    <div class="owner">Dana Corvell, President / Owner</div>
    <div><svg width="16" height="12" viewBox="0 0 16 12"><rect x="1" y="1" width="14" height="10" fill="none" stroke="#fff" stroke-width="1.5"/><path d="M1 1l7 6 7-6" fill="none" stroke="#fff" stroke-width="1.5"/></svg>dana@brantlofts.com</div>
    <div><svg width="16" height="16" viewBox="0 0 16 16"><circle cx="8" cy="8" r="6.5" fill="none" stroke="#fff" stroke-width="1.5"/><path d="M1.5 8h13M8 1.5c3 3 3 10 0 13M8 1.5c-3 3-3 10 0 13" fill="none" stroke="#fff" stroke-width="1.2"/></svg>www.brantlofts.com</div>
  </div>
</section>

<section class="card card--back">
  <div class="abs back-photo" role="img" aria-label="Faint photo of an apartment interior"></div>
  <div class="abs bar package-bar">APARTMENT PACKAGE $150</div>
  <ul class="abs bullets">
    <li>Detailed photos and documentation of larger, higher priced items such as electronics and furniture</li>
    <li>Back-up copy of inventory on disc</li>
    <li>Full color printed binder with report &amp; photos</li>
    <li>Up to 25 photos</li>
  </ul>
  <div class="abs callbox">
    <div class="heading">Call us</div>
    <div class="phone">602-555-0143</div>
    <div class="mail">dana@brantlofts.com</div>
    <div class="mail">www.brantlofts.com</div>
  </div>
  <p class="abs note">***If your home has an above average amount of contents, the amount of photos needed to document your home's inventory may exceed what's included in your package. If additional photos are requested, there will be a charge of $1 per every photo above what's included in your chosen package.</p>
  <div class="abs bar services-bar">ADDITIONAL SERVICES</div>
  <ul class="abs services">
    <li>Clothing Inventory - <b>$10</b> per item (All packages include general photos of closets and open drawers. This package includes individual documentation of higher priced individual pieces such as designer jeans, suits, dresses etc.)</li>
    <li>Collectibles / Antiques / Sports Equipment - <b>$50</b> (Includes individual photos and upload of available receipts or appraisals)</li>
    <li>Dishware / Silverware - <b>$50</b> (Includes individual photos and upload of available receipts)</li>
    <li>Jewelry - <b>$15</b> per item (Includes individual photos and upload of available receipts or appraisals)</li>
    <li>Shed / Detached garage inventory - <b>$1</b> per square footage of the shed. Includes up to 10 photos</li>
    <li>Additional inventory update - <b>$50</b> per hour (Minimum of 1 hour)</li>
    <li>Insurance Consultation with your current insurance Declarations page - <b>$100</b> (Up to a 2 hour visit)</li>
  </ul>
</section>

</body>
</html>
```